Limousine Service Company Website

we need a website designed for a Meridian Limousine Company with global capabilities (meaning they can service clients throughout the US and the world)

They service mostly corporate/business travelers, and groups and meetings, with a small portion of their business devoted to retail clients (special events and personal travel)

The overall look should be corporate, and we prefer a responsive design. We will need a home page, a fleet page (examples can be seen here: https://www.brqcarriage.com/fleet
http://www.pellowaychauffeurs.com/our-fleet) and one interior page

Copy will be lorem epsum for now

We have no logo yet but can put a placeholder logo

Industry/Entity Type

It Company

```html
<!DOCTYPE html>
<html lang="en">
<head>
<meta charset="utf-8">
<title>Meridian Limousine Company</title>
<link href="https://fonts.googleapis.com/css2?family=Ubuntu:wght@400;500&family=Arimo:wght@400;700&display=swap" rel="stylesheet">
<style>
:root{
  --bg:#131313;
  --bg-soft:#1a1a1a;
  --blue:#0a74c6;
  --nav-active:#1b1b1b;
  --white:#ffffff;
  --text:#f2f2f2;
  --icon:#e6e6e6;
  --green:#7cc13a;
  --orange:#f08a1c;
  --divider:#2c2c2c;
}
*{margin:0;padding:0;box-sizing:border-box}
html,body{width:1056px;height:1200px;overflow:hidden;background:var(--bg);color:var(--text);font-family:"Arimo",Arial,sans-serif}
.page{position:relative;width:1056px;height:1200px;overflow:hidden}
.site-header{height:167px;position:relative}
.brand{position:absolute;left:44px;top:58px;display:flex;align-items:center;gap:12px}
.brand-dot{width:26px;height:26px;border-radius:50%;background:var(--blue)}
.brand-name{font-family:"Ubuntu",sans-serif;font-size:19px;color:var(--white);font-weight:400}
.contact{position:absolute;left:837px;top:66px;font-size:12px;font-weight:700;color:var(--white);line-height:26px}
.contact .phone{display:flex;align-items:center;gap:8px;margin-bottom:8px}
.main-nav{height:50px;background:var(--blue);display:flex;padding-left:46px}
.main-nav a{display:flex;align-items:center;justify-content:center;height:50px;color:var(--white);text-decoration:none;font-size:13px;border-right:1px solid rgba(0,0,0,.12)}
.main-nav a.active{background:var(--nav-active)}
.hero{position:relative;height:441px;border-bottom:2px solid var(--orange);background:linear-gradient(180deg,#3c4a2c 0%,#4c5a3a 25%,#c9cfd3 45%,#e6e8ea 60%,#6f7377 80%,#5a5e61 100%)}
.hero-caption{position:absolute;left:124px;top:27px;width:809px;height:120px;background:rgba(20,20,20,.6);padding:7px 26px;font-family:"Ubuntu",sans-serif;font-size:22px;line-height:35px;color:var(--green)}
.slider-arrows{position:absolute;top:677px;left:490px;display:flex;gap:14px}
.features{position:absolute;top:752px;left:0;width:1056px;display:flex}
.feature{width:345px;text-align:center;padding:0 0 0 0;position:relative}
.feature + .feature{border-left:1px solid var(--divider)}
.feature h2{font-weight:400;font-size:25px;color:var(--white);margin-top:2px;letter-spacing:.3px}
.feature .icon{height:96px;display:flex;align-items:center;justify-content:center;margin-top:10px}
.feature p{text-align:justify;font-size:12px;line-height:21px;margin:27px 0 0 0;letter-spacing:.2px}
.feature:nth-child(1) p{margin-left:44px;margin-right:26px}
.feature:nth-child(2) p{margin-left:33px;margin-right:30px}
.feature:nth-child(3) p{margin-left:35px;margin-right:14px}
.more{display:inline-block;vertical-align:middle;margin-left:6px}
.lower{position:absolute;top:1041px;left:0;width:1056px;height:159px;background:var(--bg-soft)}
.about{position:absolute;left:44px;top:22px;width:292px}
.events{position:absolute;left:367px;top:22px;width:300px}
.lower h2{font-weight:400;font-size:25px;color:var(--white);margin-bottom:17px}
.lower p{font-size:12px;line-height:21px;margin-bottom:20px}
.events .lead{color:var(--orange)}
.car-visual{position:absolute;left:691px;top:34px;width:322px;height:95px;border-radius:30px 40px 12px 12px;background:linear-gradient(180deg,#f4f4f4,#c9c9c9)}
</style>
</head>
<body>
<div class="page">
  <header class="site-header">
    <div class="brand"><span class="brand-dot"></span><span class="brand-name">Meridian Limousine Company</span></div>
    <div class="contact">
      <div class="phone">
        <svg width="16" height="20" viewBox="0 0 16 20"><path d="M4 1 L7 5 L5 7 C6 10 8 13 10 14 L12 12 L15 16 L12 19 C6 18 1 11 1 4 Z" fill="#fff"/></svg>
        <span>(100) 555-01847</span>
      </div>
      <div>418 Harlow Street Elm Ridge,</div>
      <div>country 10622</div>
    </div>
  </header>
  <nav class="main-nav">
    <a class="active" href="#" style="width:99px">HOME</a>
    <a href="#" style="width:100px">FLEET</a>
    <a href="#" style="width:99px">INTERIOR</a>
    <a href="#" style="width:99px">CONTACTS</a>
  </nav>
  <section class="hero" role="img" aria-label="Photo of a white stretch limousine parked beside trees">
    <div class="hero-caption">At Meridian Limousine, we use our experience, commitment and focus on quality, to provide the finest chauffeured ground transportation services throughout the world</div>
  </section>
  <div class="slider-arrows">
    <svg width="32" height="32" viewBox="0 0 32 32"><circle cx="16" cy="16" r="15" fill="#222"/><path d="M7 16 L15 9 V13 H25 V19 H15 V23 Z" fill="#0a74c6"/></svg>
    <svg width="32" height="32" viewBox="0 0 32 32"><circle cx="16" cy="16" r="15" fill="#222"/><path d="M25 16 L17 9 V13 H7 V19 H17 V23 Z" fill="#0a74c6"/></svg>
  </div>
  <section class="features">
    <article class="feature">
      <h2>FAST &amp; SAFE</h2>
      <div class="icon"><svg width="84" height="84" viewBox="0 0 84 84"><circle cx="42" cy="42" r="36" fill="none" stroke="#e6e6e6" stroke-width="10"/><path d="M38 22 V46 H58" fill="none" stroke="#e6e6e6" stroke-width="8"/></svg></div>
      <p>Lorem ipsum dolor sit amet conse ctetur adipisic-ing elit, sed do eiusmod tempor incididunt ut labore et dolore magna aliqua. Ut enim ad minim veniam, quis nostrud. <svg class="more" width="20" height="20" viewBox="0 0 20 20"><circle cx="10" cy="10" r="10" fill="#0a74c6"/><path d="M15 10 L10 5.5 V8 H5 V12 H10 V14.5 Z" fill="#fff"/></svg></p>
    </article>
    <article class="feature">
      <h2>BEST PRICES</h2>
      <div class="icon"><svg width="80" height="86" viewBox="0 0 80 86"><rect x="2" y="38" width="16" height="42" rx="3" fill="#e6e6e6"/><path d="M22 40 L38 14 C40 6 48 4 50 10 L47 32 H70 C78 33 80 40 75 46 C79 50 77 56 73 58 C76 62 73 68 68 69 C70 74 66 80 60 80 H22 Z" fill="none" stroke="#e6e6e6" stroke-width="6" stroke-linejoin="round"/></svg></div>
      <p>Lorem ipsum dolor sit amet conse ctetur adipisic-ing elit, sed do eiusmod tempor incididunt ut labore et dolore magna aliqua. Ut enim ad minim veniam, quis nostrud. <svg class="more" width="20" height="20" viewBox="0 0 20 20"><circle cx="10" cy="10" r="10" fill="#0a74c6"/><path d="M15 10 L10 5.5 V8 H5 V12 H10 V14.5 Z" fill="#fff"/></svg></p>
    </article>
    <article class="feature" style="width:366px">
      <h2>RENTAL SERVICE</h2>
      <div class="icon"><svg width="88" height="76" viewBox="0 0 88 76"><path d="M30 14 V6 H58 V14" fill="none" stroke="#e6e6e6" stroke-width="6"/><rect x="0" y="14" width="12" height="62" rx="5" fill="#e6e6e6"/><rect x="16" y="14" width="56" height="62" fill="#e6e6e6"/><rect x="76" y="14" width="12" height="62" rx="5" fill="#e6e6e6"/></svg></div>
      <p>Lorem ipsum dolor sit amet conse ctetur adipisic-ing elit, sed do eiusmod tempor incididunt ut labore et dolore magna aliqua. Ut enim ad minim veniam, quis nostrud. <svg class="more" width="20" height="20" viewBox="0 0 20 20"><circle cx="10" cy="10" r="10" fill="#0a74c6"/><path d="M15 10 L10 5.5 V8 H5 V12 H10 V14.5 Z" fill="#fff"/></svg></p>
    </article>
  </section>
  <section class="lower">
    <div class="about">
      <h2>ABOUT</h2>
      <p>Lorem ipsum dolor sit amet conse ctetur adipisicing elit, sed do eiusmod tempor incididunt ut labore et dolore magna aliqua.</p>
      <p>Ut enim ad minim veniam, quis nostrud exercitation</p>
    </div>
    <div class="events">
      <h2>OUR EVENTS</h2>
      <p class="lead">Lorem ipsum dolor sit amet conse ctetur adipisicing elit, sed do eiusmod tempor</p>
      <p>Ut enim ad minim veniam, quis nostrud exercitation ullamco laboris nisi ut aliquip ex ea commodo</p>
    </div>
    <div class="car-visual" role="img" aria-label="Side view of a white stretch limousine"></div>
  </section>
</div>
</body>
</html>
```